Labour Hire App - Screen and Logo Design

I have about 15-30 screens I need designed. They are pretty basic as long as they follow the same style guide.
I've got rough wire framing I just need a logo, style guide & screens designed.

The idea behind the app is to provide workplaces and workers a quick and easy solution to their labour and equipment needs.

Target Market(s)

Construction and labour force

Industry/Entity Type

Construction

Font styles to use
Serif

Colors
faa54b
f37122
abd037
9bcb3c

Requirements
Must have
• Each of the displayed screens need to be represented.

```html
<!DOCTYPE html>
<html lang="en">
<head>
<meta charset="utf-8">
<title>Employer Sign Up</title>
<link rel="stylesheet" href="https://fonts.googleapis.com/css2?family=Questrial&display=swap">
<style>
  :root {
    --ink-light: #ffffff;
    --ink-soft: #e6e6e6;
    --rule: rgba(255,255,255,0.55);
    --rule-faint: rgba(255,255,255,0.18);
    --field-bg: #ebebeb;
    --field-line: #8a8a8a;
    --field-label: #5a5a5a;
    --photo-dark: #2f3236;
    --photo-steel: #5b636d;
    --photo-warm: #8a6a3c;
    --photo-spark: #c58a3d;
  }
  * { box-sizing: border-box; margin: 0; padding: 0; }
  html, body { width: 676px; height: 1200px; overflow: hidden; background: var(--photo-dark); }
  body { font-family: "Questrial", sans-serif; color: var(--ink-light); }
  .screen { position: relative; width: 676px; height: 1200px; overflow: hidden; }
  .screen-photo {
    position: absolute; inset: 0;
    background:
      radial-gradient(ellipse 260px 180px at 470px 760px, rgba(214,170,70,0.75), transparent 70%),
      radial-gradient(ellipse 300px 240px at 520px 980px, rgba(200,130,60,0.55), transparent 70%),
      radial-gradient(ellipse 220px 300px at 170px 420px, rgba(110,100,95,0.6), transparent 70%),
      linear-gradient(160deg, #3a3d42 0%, var(--photo-steel) 35%, #4f4a44 60%, var(--photo-warm) 80%, #3c2e22 100%);
  }
  .screen-shade { position: absolute; inset: 0; background: rgba(20,22,26,0.25); }
  .status-bar { position: absolute; top: 0; left: 0; width: 676px; height: 44px; }
  .status-time { position: absolute; top: 10px; width: 100%; text-align: center; font-size: 21px; }
  .status-battery-text { position: absolute; top: 10px; right: 62px; font-size: 21px; }
  .back-button { position: absolute; left: 30px; top: 68px; }
  .screen-title { position: absolute; top: 68px; width: 100%; text-align: center; font-size: 34px; letter-spacing: 0.5px; }
  .section-heading { position: absolute; left: 58px; font-size: 34px; letter-spacing: 0.5px; }
  .field { position: absolute; left: 102px; width: 450px; font-size: 29px; color: var(--ink-soft); letter-spacing: 1px; border-bottom: 1px solid var(--rule-faint); padding-bottom: 4px; }
  .divider { position: absolute; left: 32px; width: 610px; height: 1px; background: var(--rule); }
  .card-form { position: absolute; left: 32px; top: 772px; width: 612px; height: 199px; background: var(--field-bg); border-radius: 8px; overflow: hidden; }
  .card-cell { position: absolute; font-size: 23px; color: var(--field-label); letter-spacing: 1px; padding: 6px 6px; }
  .card-line { position: absolute; background: var(--field-line); }
  .submit-button { position: absolute; left: 80px; top: 1044px; width: 526px; height: 67px; border: 1px solid var(--ink-light); background: transparent; color: var(--ink-light); font-family: "Questrial", sans-serif; font-size: 36px; }
</style>
</head>
<body>
<main class="screen">
  <div class="screen-photo" role="img" aria-label="Blurred background photo of a welder cutting steel with sparks flying"></div>
  <div class="screen-shade"></div>

  <div class="status-bar">
    <svg width="120" height="44" style="position:absolute;left:14px;top:0">
      <g fill="#fff" stroke="#fff" stroke-width="1.5">
        <circle cx="8" cy="22" r="5"/><circle cx="22" cy="22" r="5"/><circle cx="36" cy="22" r="5"/>
        <circle cx="50" cy="22" r="4.5" fill="none"/><circle cx="64" cy="22" r="4.5" fill="none"/>
      </g>
      <g fill="none" stroke="#fff" stroke-width="2.6" stroke-linecap="round">
        <path d="M84 18 a14 14 0 0 1 20 0"/><path d="M88 22 a8 8 0 0 1 12 0"/>
      </g>
      <circle cx="94" cy="27" r="2.4" fill="#fff"/>
    </svg>
    <div class="status-time">4:39 PM</div>
    <div class="status-battery-text">100%</div>
    <svg width="50" height="44" style="position:absolute;right:8px;top:0">
      <rect x="2" y="14" width="40" height="17" rx="3" fill="none" stroke="#fff" stroke-width="1.5"/>
      <rect x="5" y="17" width="34" height="11" rx="1.5" fill="#fff"/>
      <rect x="43" y="19" width="3" height="7" rx="1" fill="#fff"/>
    </svg>
  </div>

  <svg class="back-button" width="30" height="48" aria-label="Back">
    <path d="M26 2 L4 24 L26 46" fill="none" stroke="#fff" stroke-width="3"/>
  </svg>
  <h1 class="screen-title" style="font-weight:400">Employer Sign Up</h1>

  <h2 class="section-heading" style="top:200px;font-weight:400">Account:</h2>
  <div class="field" style="top:262px">Email</div>
  <div class="field" style="top:323px">Password</div>
  <div class="divider" style="top:393px"></div>

  <h2 class="section-heading" style="top:420px;font-weight:400">Profile:</h2>
  <div class="field" style="top:474px">First name</div>
  <div class="field" style="top:535px">Mobile number</div>
  <div class="field" style="top:594px;padding-left:6px">Language</div>
  <div class="divider" style="top:669px"></div>

  <h2 class="section-heading" style="top:697px;font-weight:400">Payment:</h2>
  <div class="card-form">
    <div class="card-line" style="left:404px;top:0;width:1px;height:199px"></div>
    <div class="card-line" style="left:0;top:100px;width:612px;height:1px"></div>
    <div class="card-line" style="left:202px;top:100px;width:1px;height:99px"></div>
    <div class="card-cell" style="left:0;top:0">Credit Cart Number</div>
    <div class="card-cell" style="left:404px;top:0">CVV</div>
    <div class="card-cell" style="left:0;top:100px">Expiration Date</div>
    <div class="card-cell" style="left:404px;top:100px">Poscode</div>
  </div>

  <button class="submit-button" type="button">Sign Up</button>
</main>
</body>
</html>
```